Social News web page design website name Vorlet.

I need a web design for a start up project called Vorlet based in Sydney. Its a social news website. it helps people to get centralized news and people can have their own profiles where they can post there thoughts and comments and it will be free to signup and usage as well.

I would like to see designs that use the latest pelican scaffold framework and are mobile compatible. only need 2 pages a home page kind of similar to
plonk (http://plonk.example/) and a profile that's a next gen user profile page I will leave that to you imaginations

this is my previous design I did on my own http://www.vorlet.example/

Target Market(s)

target market is 13 and up and anyone who likes or uses social media and would be able to understand the site

Industry/Entity Type

News

Requirements
Must have
• 1.) using pelican scaffold. 2) a home page similar to plonk (http://plonk.example/) or even better free to use your imagination 3) a next gen profile page better the one i made on my own which is this one (http://www.vorlet.example/profile/hollisbrackett) 4) for mobile navigation, have a mobile navigation something similar to http://slidepanel.quenrow.example/
Nice to have
• 1) a sexy navigation and layout for both desktop and mobile phones. i will leave that to you imaginations. 2) social medial buttons like to sign-in with and also to post a story to Chatterly or pelican 3) a user settings page (but not necessary) 4) a login or signup (but not necessary)

```html
<!DOCTYPE html>
<html lang="en">
<head>
<meta charset="utf-8">
<title>Vorlet — Social News</title>
<link rel="stylesheet" href="https://fonts.googleapis.com/css2?family=Oswald:wght@400;500&family=Libre+Baskerville:wght@400;700&family=Roboto:wght@400;500;700&display=swap">
<style>
  :root{
    --accent:#e8173f;
    --ink:#1a1a1a;
    --body-text:#444;
    --muted:#8a8a8a;
    --bar:#111;
    --bar-deep:#060606;
    --panel:#f2f2f2;
    --page-bg-a:#c6c6c6;
    --page-bg-b:#dcdcdc;
    --white:#fff;
    --rule:#2a2a2a;
  }
  *{box-sizing:border-box;margin:0;padding:0}
  html,body{width:1058px;height:1200px;overflow:hidden}
  body{
    background:linear-gradient(90deg,var(--page-bg-a),var(--page-bg-b) 30%,var(--page-bg-a) 60%,var(--page-bg-b));
    font-family:'Roboto',Arial,sans-serif;color:var(--body-text);
  }
  a{color:inherit;text-decoration:none}
  .page{position:absolute;left:85px;top:0;width:889px;height:1200px;background:var(--white)}

  /* top navigation */
  .topnav{position:absolute;left:0;top:0;width:100%;height:43px;background:var(--bar)}
  .topnav ul{list-style:none}
  .topnav li{position:absolute;top:0;height:43px;line-height:43px;font-family:'Oswald',sans-serif;font-size:13px;color:var(--white);text-transform:uppercase}
  .topnav li.is-active{left:0;width:59px;background:var(--bar-deep);color:var(--accent);padding-left:15px}
  .search{position:absolute;left:721px;top:9px;width:152px;height:24px;display:flex}
  .search input{width:129px;height:24px;border:0;background:var(--bar-deep);color:#999;font:10px 'Roboto',sans-serif;padding-left:8px}
  .search button{width:23px;height:24px;border:0;background:var(--accent);display:flex;align-items:center;justify-content:center}

  /* masthead */
  .masthead{position:absolute;left:0;top:43px;width:100%;height:87px}
  .brand{position:absolute;left:17px;top:26px;font-family:'Libre Baskerville',serif;font-weight:700;font-size:28px;color:var(--ink);letter-spacing:-.5px}
  .social{position:absolute;left:622px;top:28px;display:flex;gap:5.5px}
  .social span{width:27px;height:27px;border-radius:50%;background:#2b2b2b;display:block}
  .band{position:absolute;left:0;top:130px;width:100%;height:15px;background:var(--bar)}

  /* section titles */
  .section-title{font-family:'Oswald',sans-serif;font-weight:500;font-size:14px;color:var(--accent);text-transform:uppercase;letter-spacing:-.2px;line-height:1}
  .rule-solid{height:2px;background:var(--rule)}
  .rule-hatched{height:4px;background:repeating-linear-gradient(135deg,#ddd 0 1px,transparent 1px 3px)}

  /* breaking news */
  .breaking{position:absolute;left:15px;top:165px;width:323px}
  .breaking .rule-solid{margin-top:11px}
  .slider{position:absolute;left:0;top:42px;width:323px;height:273px;background:linear-gradient(120deg,#cfcfcf,#8d8d8d 45%,#3a3a3a 80%,#6b6b6b)}
  .slider-arrow{position:absolute;top:104px;width:25px;height:44px;background:#0d0d0d;display:flex;align-items:center;justify-content:center}
  .slider-arrow.prev{left:0}.slider-arrow.next{right:0}
  .slider-caption{position:absolute;left:0;bottom:0;width:100%;height:58px;background:rgba(40,40,40,.78);padding:8px 0 0 16px}
  .tag{display:inline-block;background:#555;color:#ddd;font:500 8px 'Roboto',sans-serif;padding:3px 4px;text-transform:uppercase}
  .slider-caption h2{font-family:'Libre Baskerville',serif;font-weight:700;font-size:18px;color:var(--white);margin-top:3px;white-space:nowrap}

  /* meta line */
  .meta{font-size:8.5px;font-weight:700;color:#333;line-height:12px}
  .meta .in,.meta .sep{color:var(--accent);font-weight:400}
  .meta .sep{margin:0 3px}

  /* entertainment list */
  .entertainment{position:absolute;left:15px;top:496px;width:323px;height:403px;background:var(--panel);padding:21px 16px 0;overflow:hidden}
  .entertainment .rule-solid{margin-top:9px;margin-bottom:16px}
  .ent-item{display:flex;height:101px;margin-bottom:13px;border-bottom:1px solid #ddd}
  .ent-item:last-child{border-bottom:0;margin-bottom:0}
  .ent-item .thumb{flex:0 0 118px;height:82px;margin-right:16px}
  .ent-body{flex:1;min-width:0}
  .ent-item h3{font-family:'Libre Baskerville',serif;font-size:12px;color:var(--ink);font-weight:400;line-height:15px;margin:6px 0 4px;letter-spacing:-.2px}
  .ent-item p{font-size:9.3px;line-height:13.5px}

  /* categories */
  .categories{position:absolute;left:15px;top:899px;width:323px;height:167px;background:var(--bar);padding:22px 16px 0;display:flex;gap:15px}
  .categories section{width:138px}
  .categories h4{font-family:'Oswald',sans-serif;font-weight:400;font-size:11px;color:#ddd;text-transform:uppercase}
  .categories .line{height:2px;background:#3a3a3a;margin:8px 0 12px}
  .categories ul{list-style:none}
  .categories li{font-size:10px;color:#bbb;line-height:19.7px}

  /* latest news */
  .latest{position:absolute;left:354px;top:165px;width:520px}
  .latest .rule-hatched{margin-top:11px}
  .card{position:absolute;width:118px}
  .card.wide{width:252px}
  .card .photo{width:100%;height:118px;margin-bottom:10px;position:relative}
  .card.wide .photo{height:173px;margin-bottom:10px}
  .card h3{font-family:'Libre Baskerville',serif;font-weight:400;font-size:11.5px;line-height:14.5px;color:var(--ink);margin:8px 0 3px;letter-spacing:-.2px}
  .card.wide h3{font-size:14.5px;line-height:19px;margin:6px 0 4px}
  .card p{font-size:9.3px;line-height:14px}
  .play{position:absolute;left:100px;top:70px}

  /* footer */
  .footer{position:absolute;left:0;top:1082px;width:100%;height:118px;background:var(--bar)}
  .footer-brand{position:absolute;left:11px;top:14px;font-family:'Libre Baskerville',serif;font-weight:700;font-size:25px;color:#2c2c2c}
  .footer .line{position:absolute;left:15px;top:55px;width:859px;height:1px;background:#2a2a2a}
  .footer-links{position:absolute;left:15px;top:82px;display:flex;list-style:none;font-size:10px;color:#aaa}
  .footer-links li+li::before{content:"";display:inline-block;width:1px;height:12px;background:#444;margin:0 16px;vertical-align:middle}
  .copyright{position:absolute;left:607px;top:82px;font-size:10px;color:#ccc}
</style>
</head>
<body>
<div class="page">

  <nav class="topnav">
    <ul>
      <li class="is-active">Home</li>
      <li style="left:74px">Video</li>
      <li style="left:133px">Reader</li>
      <li style="left:202px">Submit Story</li>
      <li style="left:304px">Contact</li>
    </ul>
    <form class="search">
      <input type="text" placeholder="Search">
      <button type="button" aria-label="Search">
        <svg width="11" height="11" viewBox="0 0 11 11"><circle cx="4.5" cy="4.5" r="3.3" fill="none" stroke="#fff" stroke-width="1.6"/><line x1="7" y1="7" x2="10" y2="10" stroke="#fff" stroke-width="1.8"/></svg>
      </button>
    </form>
  </nav>

  <header class="masthead">
    <div class="brand">Vorlet</div>
    <div class="social" aria-label="Social network links">
      <span></span><span></span><span></span><span></span><span></span><span></span><span></span><span></span>
    </div>
  </header>
  <div class="band"></div>

  <section class="breaking">
    <h2 class="section-title">Breaking News</h2>
    <div class="rule-solid"></div>
    <div class="slider" role="img" aria-label="Featured photo: portrait of a woman with windswept dark hair">
      <span class="slider-arrow prev"><svg width="12" height="20" viewBox="0 0 12 20"><polyline points="10,2 2,10 10,18" fill="none" stroke="#fff" stroke-width="1.6"/></svg></span>
      <span class="slider-arrow next"><svg width="12" height="20" viewBox="0 0 12 20"><polyline points="2,2 10,10 2,18" fill="none" stroke="#fff" stroke-width="1.6"/></svg></span>
      <div class="slider-caption">
        <span class="tag">Feature</span>
        <h2>Etiam porta sem malesuada</h2>
      </div>
    </div>
  </section>

  <section class="entertainment">
    <h2 class="section-title">Entertaiment</h2>
    <div class="rule-solid"></div>
    <article class="ent-item">
      <div class="thumb" role="img" aria-label="Photo: woman wearing a beaded veil" style="background:linear-gradient(160deg,#3b2418,#8a5a3a 55%,#2a1a12)"></div>
      <div class="ent-body">
        <div class="meta"><span class="in">in:</span> Entertaiment<span class="sep">|</span>July 19, 2012</div>
        <h3>Who made dummy text?</h3>
        <p>Lorem ipsum dolor sit amet, consectetuer adipiscing elit. Aenean commodo ligula</p>
      </div>
    </article>
    <article class="ent-item">
      <div class="thumb" role="img" aria-label="Photo: bronze statue against a blue sky" style="background:linear-gradient(180deg,#bcd3e6,#8fb2cf 60%,#6f5a44)"></div>
      <div class="ent-body">
        <div class="meta"><span class="in">in:</span> Entertaiment<span class="sep">|</span>July 19, 2012</div>
        <h3>We Can make it happen</h3>
        <p>Lorem ipsum dolor sit amet, consectetuer adipiscing elit. Aenean commodo ligula</p>
      </div>
    </article>
    <article class="ent-item">
      <div class="thumb" role="img" aria-label="Photo: spiral seashell on black" style="background:radial-gradient(circle at 55% 55%,#d9c6a8,#6d5a44 35%,#0b0b0b 70%)"></div>
      <div class="ent-body">
        <div class="meta"><span class="in">in:</span> Entertaiment<span class="sep">|</span>July 18, 2012</div>
        <h3>Tower on The Great Wall of China</h3>
        <p>Lorem ipsum dolor sit amet, consectetuer adipiscing elit. Aenean commodo ligula</p>
      </div>
    </article>
  </section>

  <aside class="categories">
    <section>
      <h4>Categories</h4>
      <div class="line"></div>
      <ul><li>Entertaiment</li><li>Feature</li><li>Life style</li><li>Travel</li><li>Uncategorized</li></ul>
    </section>
    <section>
      <h4>Categories</h4>
      <div class="line"></div>
      <ul><li>Entertaiment</li><li>Feature</li><li>Life style</li><li>Travel</li><li>Uncategorized</li></ul>
    </section>
  </aside>

  <section class="latest">
    <h2 class="section-title">Latest News</h2>
    <div class="rule-hatched"></div>

    <article class="card" style="left:0;top:44px">
      <div class="photo" role="img" aria-label="Photo: portrait of a blonde woman" style="background:linear-gradient(150deg,#c89a5a,#e7c58f 45%,#4a2e1a)"></div>
      <div class="meta"><span class="in">in:</span> Travel<span class="sep">|</span>October 3, 2012</div>
      <h3>Black hole to eat planetary cloud</h3>
      <p>Lorem ipsum dolor sit amet, consectetuer adipiscing elit. Aenean commodo ligula. Lorem ipsum dolor sit amet, consectetuer adipiscing elit. Aenean commodo ligula</p>
    </article>

    <article class="card" style="left:134px;top:44px">
      <div class="photo" role="img" aria-label="Photo: woman wearing a beaded veil" style="background:linear-gradient(160deg,#2e1c14,#7d5136 55%,#1e120c)"></div>
      <div class="meta"><span class="in">in:</span> Entertaiment<span class="sep">|</span>July 19, 2012</div>
      <h3>Who made dummy text?</h3>
      <p>Lorem ipsum dolor sit amet, consectetuer adipiscing elit. Aenean commodo ligula</p>
    </article>

    <article class="card wide" style="left:268px;top:44px">
      <div class="photo" role="img" aria-label="Video still: two women posed in front of a weathered wooden wall" style="background:linear-gradient(100deg,#7d7a70,#b5b0a2 45%,#e2dccd 70%,#9a9486)">
        <svg class="play" width="12" height="18" viewBox="0 0 12 18"><polygon points="0,0 12,9 0,18" fill="#111"/></svg>
      </div>
      <div class="meta"><span class="in">in:</span> Entertaiment<span class="sep">|</span>July 19, 2012</div>
      <h3>Hartwell: Does ‘Midnight Harbor’ have it…</h3>
      <p>Lorem ipsum dolor sit amet, consectetuer adipiscing elit. Aenean commodo ligula</p>
    </article>

    <article class="card" style="left:0;top:349px">
      <div class="photo" role="img" aria-label="Photo: woman in a red top among tall grass" style="background:linear-gradient(170deg,#a9b0b8,#c7a57a 45%,#b8442f 75%,#8a6a45)"></div>
      <div class="meta"><span class="in">in:</span> Entertaiment<span class="sep">|</span>July 19, 2012</div>
      <h3>Food styling workshop</h3>
      <p>Lorem ipsum dolor sit amet, consectetuer adipiscing elit. Aenean commodo ligula</p>
    </article>

    <article class="card" style="left:134px;top:349px">
      <div class="photo" role="img" aria-label="Photo: man and horse at a wooden fence under trees" style="background:linear-gradient(170deg,#4f7a3a,#8aa865 45%,#7a5a3c 70%,#9c958a)"></div>
      <div class="meta"><span class="in">in:</span> Entertaiment<span class="sep">|</span>July 19, 2012</div>
      <h3>Food and Drink consultancy</h3>
      <p>Lorem ipsum dolor sit amet, consectetuer adipiscing elit. Aenean commodo ligula</p>
    </article>

    <article class="card wide" style="left:268px;top:329px">
      <div class="photo" role="img" aria-label="Video still: bronze statue against a cloudy blue sky" style="background:linear-gradient(180deg,#a9c6df,#cddbe6 45%,#6e5840 75%,#4e3e2d)">
        <svg class="play" width="12" height="18" viewBox="0 0 12 18"><polygon points="0,0 12,9 0,18" fill="#111"/></svg>
      </div>
      <div class="meta"><span class="in">in:</span> Entertaiment<span class="sep">|</span>July 19, 2012</div>
      <h3>We Can make it happen</h3>
      <p>Lorem ipsum dolor sit amet, consectetuer adipiscing elit. Aenean commodo ligula</p>
    </article>
  </section>

  <footer class="footer">
    <div class="footer-brand">Vorlet</div>
    <div class="line"></div>
    <ul class="footer-links">
      <li>About</li><li>Privacy Policy</li><li>FAQ</li><li>Term of Use</li>
    </ul>
    <div class="copyright">Copyright © 2014 Vorlet. All rights reserved</div>
  </footer>

</div>
</body>
</html>
```